Business Card Design For Financial Company

Create a new design for company's business card. The corporate logo is attached in several formats. Our new website design is also attached and we would like the business cards to reflect this.
Card needs to contain the following info:
Name
Job Title
Legal company name - eg Varomel Holdings (Asia) Ltd
Address - eg 517-09 Brellford Plaza,46 Tamsworth Lane, Hong Kong
Direct tel
Main tel
Fax
Email
Website URL
MS word format preferred. Other formats that can be edited on standard PC also OK.
Updates
Please note the the "VAROMEL" logo nameĀ font is "Gill Sans MT" on Windows
Target Market(s)
Instituation Investors
Industry/Entity Type
Business
Look and feel
Each slider illustrates characteristics of the customer's brand and the style your logo design should communicate.

```html
<!DOCTYPE html>
<html lang="en">
<head>
<meta charset="utf-8">
<title>Varomel Holdings – Business Card</title>
<link rel="stylesheet" href="https://fonts.googleapis.com/css2?family=Lato:wght@300;400&display=swap">
<style>
  :root {
    --backdrop: #97a1a7;
    --card: #ffffff;
    --brand-red: #d0101e;
    --ink: #1d1d1d;
    --ink-soft: #333333;
    --placeholder: #c9cdd0;
    --on-red: #ffffff;
  }
  * { box-sizing: border-box; margin: 0; padding: 0; }
  html, body {
    width: 1200px; height: 900px; overflow: hidden;
    background: var(--backdrop);
    font-family: "Lato", "Gill Sans MT", "Gill Sans", sans-serif;
  }
  .canvas { position: relative; width: 1200px; height: 900px; }
  .card {
    position: absolute; left: 335px; width: 605px; height: 368px;
    background: var(--card);
  }
  .card--front { top: 60px; }
  .card--back { top: 460px; }

  /* Front */
  .brand { position: absolute; left: 40px; top: 206px; display: flex; align-items: center; gap: 14px; }
  .brand__mark { width: 44px; height: 44px; background: var(--placeholder); }
  .brand__name { font-size: 33px; font-weight: 300; letter-spacing: 1.5px; color: var(--ink); }
  .tagline {
    position: absolute; left: 302px; top: 202px; width: 303px; height: 66px;
    background: var(--brand-red); color: var(--on-red);
    padding: 8px 0 0 20px; font-size: 19px; line-height: 26px; text-transform: uppercase;
  }

  /* Back */
  .person { position: absolute; left: 40px; top: 33px; font-size: 19px; line-height: 26px; }
  .person__name { color: var(--ink); font-weight: 400; }
  .person__title { color: var(--ink-soft); font-weight: 300; }
  .contact {
    position: absolute; right: 40px; top: 33px; text-align: right;
    font-size: 19px; line-height: 26px; font-weight: 300; color: var(--ink);
    list-style: none;
  }
  .divider {
    position: absolute; left: 40px; top: 169px; width: 565px;
    display: flex; align-items: center; gap: 10px;
  }
  .divider__rule { flex: 1; border-top: 2px dashed var(--ink); }
  .divider__url { font-size: 19px; font-weight: 300; color: var(--brand-red); padding-right: 40px; }
  .address {
    position: absolute; left: 40px; top: 228px; font-style: normal;
    font-size: 19px; line-height: 26px; font-weight: 300; color: var(--ink);
  }
  .badge {
    position: absolute; left: 446px; top: 256px; width: 159px; height: 46px;
    background: var(--brand-red); color: var(--on-red);
    display: flex; align-items: center; justify-content: center;
    font-size: 24px; font-weight: 400; letter-spacing: 1px;
  }
</style>
</head>
<body>
<main class="canvas">
  <section class="card card--front" aria-label="Card front">
    <div class="brand">
      <span class="brand__mark"></span>
      <span class="brand__name">VAROMEL</span>
    </div>
    <p class="tagline">Independent Research<br>Marketing &amp; Execution</p>
  </section>

  <section class="card card--back" aria-label="Card back">
    <div class="person">
      <p class="person__name">Daniel Reeve</p>
      <p class="person__title">Sales Manager</p>
    </div>
    <ul class="contact">
      <li>main tel: 325 555 0181</li>
      <li>direct tel: 456 555 0779</li>
      <li>fax: 012 555 0789</li>
      <li>contact@varomelholdings.com</li>
    </ul>
    <div class="divider">
      <span class="divider__rule"></span>
      <span class="divider__url">www.varomelholdings.com</span>
    </div>
    <address class="address">
      Varomel Holdings (Asia) Ltd<br>
      517-09 Brellford Plaza<br>
      46 Tamsworth Lane<br>
      Hong Kong
    </address>
    <div class="badge">VAROMEL</div>
  </section>
</main>
</body>
</html>
```